New Stationary for our business

We are a gift business and would like to create a new corporate image with new stationary and design.

We would like a Classic Corporate look with a touch of Flair.

We would need:
Envelopes
Letter Head
Business Cards
With Comp Slips
Note Pads
Etc...

Our details are:

Basket Haven Pty Ltd
518 Pelling Street, Carrow Vale, Victoria, 3071
1800 742 918
www.baskethaven.com.au
sales@baskethaven.com.au

ABN: 62 804 319 775

Target Market(s)

Corporate Look

Industry/Entity Type

Marketing

Contact Information for Business Card

Basket Haven Pty Ltd
1800 742 918
518 Pelling Street
Carrow Vale 3071
Victoria Australia

Darren Pelloni - Managing Director
darren.pelloni@baskethaven.com.au
0417 586 902

Logo Text

Basket Haven - The Present Experts

Colors

Designer to choose colors to be used in the design.

Requirements
Must have
• Look and Feel upmarket and exclusive

```html
<!DOCTYPE html>
<html lang="en">
<head>
<meta charset="utf-8">
<title>Basket Haven – Business Card</title>
<link rel="stylesheet" href="https://fonts.googleapis.com/css2?family=Roboto:wght@400;500;700&display=swap">
<style>
  :root {
    --backdrop: #3a332e;
    --card: #1d1e20;
    --ink: #f2f2f2;
    --ink-muted: #b9b9b9;
    --rule: #8c8c8c;
  }
  * { margin: 0; padding: 0; box-sizing: border-box; }
  html, body { width: 1200px; height: 769px; overflow: hidden; }
  body {
    background: var(--backdrop);
    font-family: "Roboto", Arial, sans-serif;
    color: var(--ink);
    position: relative;
  }
  .card {
    position: absolute;
    top: 236px;
    width: 520px;
    height: 297px;
    background: var(--card);
    border-radius: 4px;
    box-shadow: 0 10px 28px rgba(0,0,0,.45);
  }
  .card--back { left: 60px; }
  .card--front { left: 620px; }

  .brand {
    display: flex;
    align-items: center;
    gap: 12px;
    font-weight: 500;
    letter-spacing: .5px;
    color: var(--ink);
  }
  .brand__square {
    width: 14px; height: 14px;
    background: var(--ink);
  }
  .card--back .brand {
    position: absolute;
    left: 0; right: 0; top: 108px;
    justify-content: center;
    font-size: 34px;
    color: var(--ink-muted);
  }
  .card--back .brand__square { background: var(--ink-muted); }
  .website {
    position: absolute;
    left: 0; right: 0; top: 186px;
    text-align: center;
    font-size: 13px;
    letter-spacing: 3px;
    color: var(--ink-muted);
  }

  .card--front .brand {
    position: absolute;
    right: 36px; top: 42px;
    font-size: 34px;
  }
  .person {
    position: absolute;
    left: 36px; top: 160px;
  }
  .person__name { font-size: 17px; font-weight: 700; letter-spacing: .5px; }
  .person__role { font-size: 14px; font-weight: 500; margin-top: 4px; color: var(--ink-muted); }
  .divider {
    position: absolute;
    left: 196px; top: 148px;
    width: 1px; height: 120px;
    background: var(--rule);
  }
  .details {
    position: absolute;
    left: 216px; top: 154px;
    font-size: 14px;
    line-height: 19px;
  }
  .details__line { display: flex; align-items: center; gap: 8px; }
  .details__icon { width: 12px; height: 12px; fill: var(--ink); flex: none; }
  .details__pad { padding-left: 20px; }
</style>
</head>
<body>
  <section class="card card--back" aria-label="Card back">
    <div class="brand"><span class="brand__square"></span>Basket Haven</div>
    <p class="website">www.baskethaven.com.au</p>
  </section>

  <section class="card card--front" aria-label="Card front">
    <div class="brand"><span class="brand__square"></span>Basket Haven</div>
    <div class="person">
      <p class="person__name">MARCUS DELL</p>
      <p class="person__role">CEO/FOUNDER</p>
    </div>
    <div class="divider"></div>
    <div class="details">
      <p class="details__pad">Basket Haven Pty Ltd</p>
      <p class="details__pad">518 Pelling Street</p>
      <p class="details__pad">Carrow Vale, Victoria, 3071</p>
      <p class="details__line">
        <svg class="details__icon" viewBox="0 0 24 24" aria-hidden="true"><path d="M6.6 10.8a15.1 15.1 0 0 0 6.6 6.6l2.2-2.2a1 1 0 0 1 1-.25 11.4 11.4 0 0 0 3.6.57 1 1 0 0 1 1 1V20a1 1 0 0 1-1 1A17 17 0 0 1 3 4a1 1 0 0 1 1-1h3.5a1 1 0 0 1 1 1c0 1.25.2 2.45.57 3.57a1 1 0 0 1-.25 1z"/></svg>
        1800 742 918
      </p>
      <p class="details__line">
        <svg class="details__icon" viewBox="0 0 24 24" aria-hidden="true"><path d="M2 5h20v14H2z M3 6l9 7 9-7" fill="none" stroke="#f2f2f2" stroke-width="2"/></svg>
        sales@baskethaven.com.au
      </p>
    </div>
  </section>
</body>
</html>
```